Have you got balls? A guide to getting hands on with testicular cancer...

An informative flyer on the signs and symptoms of testicular cancer (possibly with an info graphic) and the importance of self checking regularly. As testicular cancer is the most common cancer amongst young men we would like something appealing to this age range. We are a UK based charity called Kitewing who use humour and sport to reach our target audience, however on this flyer we would prefer something generic and not sport related so that our audience can be wider.

Target Market(s)

15-49 year old men

Industry/Entity Type

Charity

Font styles to use
Sans Serif

Requirements
Must have
• Young look. Eye catching. Have Kitewing logo. Website address and social media details. Ideally something that is a nice size to pick up. I had looked at concertina cards that are credit card size and fold out.
Nice to have
• Colourful. Male appeal. We like the look of the Harbourlight Health UK charity flyers and info cards.
Should not have
• Faces of men. Sports related images.

```html
<!DOCTYPE html>
<html lang="en">
<head>
<meta charset="utf-8">
<title>Kitewing – Worried About Testicular Cancer?</title>
<link href="https://fonts.googleapis.com/css2?family=Oswald:wght@300;400;500;600;700&display=swap" rel="stylesheet">
<style>
  :root {
    --orange: #f7931e;
    --charcoal: #3b3b3b;
    --cyan: #2bc0d0;
    --lime: #b6d335;
    --teal: #1a9e8b;
    --yellow: #f6ef5b;
    --cream: #f1f4cc;
    --blue: #0fa3c5;
    --red: #a31e25;
    --figure: #1ba898;
    --figure-soft: #7fcfbf;
    --ink: #333333;
    --white: #ffffff;
  }
  * { margin: 0; padding: 0; box-sizing: border-box; }
  html, body { width: 1200px; height: 933px; overflow: hidden; }
  body { background: var(--orange); font-family: 'Oswald', sans-serif; color: var(--ink); position: relative; }

  .block { position: absolute; }
  .headline-panel { left: 0; top: 25px; width: 398px; height: 225px; background: var(--charcoal); }
  .headline-panel h1 { position: absolute; left: 42px; top: 24px; font-size: 50px; line-height: 63px; font-weight: 600; color: var(--cyan); letter-spacing: 0.3px; white-space: nowrap; }

  .about-panel { left: 0; top: 250px; width: 398px; height: 545px; background: var(--lime); padding: 37px 22px 0 25px; font-size: 16.5px; line-height: 21.6px; font-weight: 300; color: var(--ink); }
  .about-panel p { margin-bottom: 43px; }
  .about-panel strong { font-weight: 600; }
  .about-panel h3 { font-size: 16.5px; font-weight: 600; line-height: 21.6px; }

  .advice-header { left: 398px; top: 25px; width: 397px; height: 108px; background: var(--teal); text-align: center; padding-top: 17px; }
  .advice-header h2 { font-size: 24.5px; font-weight: 600; color: var(--charcoal); line-height: 30px; white-space: nowrap; }
  .advice-header p { font-size: 17px; font-weight: 600; color: var(--yellow); line-height: 21px; }

  .advice-panel { left: 398px; top: 133px; width: 397px; height: 662px; background: var(--yellow); padding: 0 22px 0 25px; font-size: 16.5px; line-height: 21.6px; font-weight: 300; }
  .stat-young { position: relative; height: 167px; }
  .stat-young .big { position: absolute; left: 38px; top: 12px; font-size: 136px; font-weight: 700; color: var(--charcoal); line-height: 130px; letter-spacing: -6px; }
  .stat-young .pct { position: absolute; left: 172px; top: 26px; font-size: 44px; font-weight: 700; color: var(--charcoal); line-height: 50px; }
  .stat-young .label { position: absolute; left: 173px; top: 82px; font-size: 23px; font-weight: 600; color: var(--charcoal); line-height: 29px; white-space: nowrap; }
  .advice-panel p { margin-bottom: 21px; }
  .signs { list-style: none; font-weight: 600; font-size: 17px; line-height: 21.8px; margin-bottom: 25px; }
  .signs li { padding-left: 10px; text-indent: -10px; }
  .signs li::before { content: "• "; }
  .advice-panel .reminder { font-size: 13.5px; }

  .footer-band { left: 0; top: 795px; width: 795px; height: 118px; background: var(--blue); }
  .brand { position: absolute; left: 42px; top: 27px; display: flex; align-items: center; gap: 12px; }
  .brand-name { font-size: 52px; font-weight: 700; color: var(--white); line-height: 60px; }
  .brand-mark { width: 18px; height: 18px; border-radius: 50%; background: var(--white); }
  .web { position: absolute; left: 475px; top: 52px; font-size: 15px; color: var(--white); font-weight: 400; letter-spacing: 0.3px; }

  .survival-panel { left: 795px; top: 25px; width: 405px; height: 888px; background: var(--cream); }
  .survival-panel .big { position: absolute; left: 58px; top: 30px; font-size: 148px; font-weight: 700; color: var(--red); line-height: 170px; letter-spacing: -1px; }
  .survival-panel .caption { position: absolute; left: 26px; top: 211px; width: 352px; font-size: 16.5px; font-weight: 600; line-height: 22px; color: var(--ink); }
  .survival-panel .source { position: absolute; left: 26px; top: 256px; font-size: 11.5px; font-weight: 300; color: var(--ink); }
  .figures-placeholder { position: absolute; left: 100px; top: 280px; width: 240px; height: 565px; background: linear-gradient(180deg, var(--figure) 0%, var(--figure-soft) 100%); }
</style>
</head>
<body>
  <section class="block headline-panel">
    <h1>Almost 50% of<br>cases are men<br>under 35</h1>
  </section>

  <section class="block about-panel">
    <p><strong>but it is one of the most treatable and curable cancers if detected early.</strong> That's why we want all young men to know about testicular cancer.</p>
    <p><strong>Our aim</strong> is to break down barriers that exist amongst young men talking about the health issues that are relevant to them and create a generation of boys and men who are knowledgable about their health from school age.</p>
    <h3>Our Mission</h3>
    <p>Our mission is to raise awareness and educate people everywhere on the issues of testicular cancer by associating with ball sports as a primary medium of branding, and to provide access to resources, information and support to those concerned or directly affected by testicular cancer.</p>
  </section>

  <header class="block advice-header">
    <h2>Worried About Testicular Cancer?</h2>
    <p>Don't fumble around in the dark<br>ask an expert for advice</p>
  </header>

  <section class="block advice-panel">
    <div class="stat-young">
      <span class="big">22</span>
      <span class="pct">%</span>
      <span class="label">Are young men aged<br>14-24 age bracket</span>
    </div>
    <p>If you find a lump or swelling in your testicles, or identify any of the signs below it's important to get it checked out by your doctor. Not all lumps are cancer so it's better to ask an expert to put your mind at rest than ignore it.</p>
    <p>There are no hard and fast rules about how often you should be checking; the most important thing is to check yourself regularly so that you know your own body, and if you find something unusual act fast.</p>
    <p>The early signs of testicular cancer are often easy to spot. Look out for one or more of the following:</p>
    <ul class="signs">
      <li>a hard lump on the front or side of a testicle</li>
      <li>swelling or enlargement of a testicle</li>
      <li>an increase in firmness of a testicle</li>
      <li>pain or discomfort in a testicle or in the scrotum (the sac that holds the testicles)</li>
      <li>an unusual difference between one testicle and the other</li>
    </ul>
    <p class="reminder">Remember, Always Be Checking and if in doubt get it checked out!</p>
  </section>

  <footer class="block footer-band">
    <div class="brand"><span class="brand-name">Kitewing</span><span class="brand-mark"></span></div>
    <span class="web">http://www.kitewing.org.uk/</span>
  </footer>

  <section class="block survival-panel">
    <span class="big">98%</span>
    <p class="caption">Survive testicular cancer for 10 or more years if detected early</p>
    <p class="source">*2010-11, England and Wales</p>
    <div class="figures-placeholder" role="img" aria-label="Pictogram grid of sixteen teal standing figures in four rows, one figure highlighted in red to show the two percent"></div>
  </section>
</body>
</html>
```